My Insurance Agency Show Display

I need to design a 10 ft x 8 ft backdrop for a show display. This is a pop up fabric most likely display that will be used for a show booth. I need someone to design something more attractive with my logo and make it more flashy so people can see and remember my company. I have attached my rough design so far. I would like it to look more modern. The photo in the design does not have to be used.

This is for an insurance agency that provides Home, Auto, Life and Health products to consumers. We also provide Renters insurance, Commercial, RV, mobile homes, and other products to our customers.

Target Market(s)

Home Owners, and Multiple Auto Owners

Industry/Entity Type

Property and Causality Insurance

Font styles to use
Sans Serif

Colors
0054AA
0677BA
7BADD7
CADEEF
E8F1F8
00AB8E
00BBA5
67D7C9
C6EFE9
E9F9F6

Requirements
Must have
• Attractive Modern Layout
Nice to have
• new and creative. Something that pops with color
Should not have
• Any affiliation to other insurance agencies.

```html
<!DOCTYPE html>
<html lang="en">
<head>
<meta charset="utf-8">
<title>Harbor Shield Agency – Show Backdrop</title>
<link rel="stylesheet" href="https://fonts.googleapis.com/css2?family=Jost:wght@400;500;600;700&family=Roboto:wght@400&display=swap">
<style>
  :root {
    --stage: #c9c9cb;
    --paper: #ffffff;
    --ink: #1f2a33;
    --brand-blue: #0054AA;
    --brand-blue-mid: #0677BA;
    --brand-teal: #00AB8E;
    --brand-teal-bright: #00BBA5;
    --text-light: #ffffff;
  }
  * { box-sizing: border-box; margin: 0; padding: 0; }
  html, body { width: 870px; height: 1200px; overflow: hidden; }
  body {
    background: var(--stage);
    font-family: "Jost", "Helvetica Neue", Arial, sans-serif;
    position: relative;
  }
  .backdrop {
    position: absolute;
    left: 20px; top: 268px;
    width: 830px; height: 663px;
    background: var(--paper);
    box-shadow: 0 3px 8px rgba(0,0,0,.25);
    overflow: hidden;
  }
  .agency-name {
    position: absolute;
    left: 0; right: 0; top: 128px;
    display: flex; align-items: center; justify-content: center; gap: 10px;
    color: var(--ink);
    font-weight: 600;
    font-size: 28px;
    line-height: 1;
    letter-spacing: 1.5px;
    text-transform: uppercase;
  }
  .agency-name .name-square {
    width: 14px; height: 14px; background: var(--brand-teal);
  }
  .brand-feature {
    position: absolute;
    left: 0; top: 196px;
    width: 195px; height: 467px;
    background: linear-gradient(160deg, var(--brand-blue-mid) 0%, var(--brand-blue) 100%);
  }
  .headline-band {
    position: absolute;
    left: 195px; top: 211px; right: 0; height: 209px;
    background: var(--ink);
  }
  .services-band {
    position: absolute;
    left: 250px; top: 420px; right: 0; height: 115px;
    background: var(--brand-teal);
  }
  .call-band {
    position: absolute;
    left: 360px; top: 535px; right: 0; height: 53px;
    background: var(--ink);
  }
  .headline {
    position: absolute; right: 38px; top: 218px;
    color: var(--brand-teal-bright);
    font-weight: 700; font-size: 76px; line-height: 1;
    letter-spacing: 0.5px;
  }
  .subhead {
    position: absolute; right: 38px; top: 297px;
    color: var(--text-light);
    font-weight: 600; font-size: 26px; line-height: 1.2;
  }
  .intro {
    position: absolute; right: 38px; top: 337px;
    width: 540px;
    color: var(--text-light);
    font-size: 11px; line-height: 16px;
    text-align: right; text-transform: uppercase;
  }
  .service-list {
    position: absolute; right: 38px; top: 424px;
    list-style: none;
    display: flex; flex-direction: column; align-items: flex-end;
    gap: 10px;
  }
  .service-row { display: flex; gap: 16px; }
  .service {
    display: flex; align-items: center; gap: 6px;
    color: var(--text-light);
    font-size: 20px; font-weight: 500; line-height: 28px;
    text-transform: uppercase;
  }
  .service svg { width: 12px; height: 12px; }
  .call-line {
    position: absolute; right: 38px; top: 537px;
    color: var(--text-light);
    font-weight: 600; font-size: 32px; line-height: 48px;
  }
  .call-line .phone { color: var(--brand-teal-bright); }
  .contact-row {
    position: absolute; right: 38px; top: 599px;
    display: flex; gap: 14px;
    font-family: "Roboto", Arial, sans-serif;
    font-size: 13px; color: var(--ink);
  }
  .contact-item { display: flex; align-items: center; gap: 5px; }
  .contact-item svg { width: 16px; height: 16px; }
</style>
</head>
<body>
<svg width="0" height="0" style="position:absolute">
  <defs>
    <symbol id="tick-box" viewBox="0 0 12 12">
      <rect x="0.75" y="0.75" width="10.5" height="10.5" fill="none" stroke="#ffffff" stroke-width="1.2"/>
      <path d="M3 6.2 L5.2 8.4 L10.5 2" fill="none" stroke="#ffffff" stroke-width="1.3"/>
    </symbol>
  </defs>
</svg>

<main class="backdrop">
  <div class="agency-name"><span class="name-square"></span>Harbor Shield Agency</div>

  <div class="brand-feature" role="img" aria-label="Large brand feature graphic in blue"></div>

  <div class="headline-band"></div>
  <div class="services-band"></div>
  <div class="call-band"></div>

  <h1 class="headline">PROTECTING</h1>
  <h2 class="subhead">WHAT MATTERS MOST TO YOU</h2>
  <p class="intro">Our comprehensive insurance services provide you with peace of mind, ensuring that your assets, health, and loved ones are safeguarded against unforeseen circumstances. Trust in our expertise to navigate the complexities of insurance and secure a brighter future for you and your family.</p>

  <ul class="service-list">
    <li class="service-row">
      <span class="service"><svg><use href="#tick-box"/></svg>Home</span>
      <span class="service"><svg><use href="#tick-box"/></svg>Auto</span>
      <span class="service"><svg><use href="#tick-box"/></svg>Life</span>
    </li>
    <li class="service-row">
      <span class="service"><svg><use href="#tick-box"/></svg>Health</span>
      <span class="service"><svg><use href="#tick-box"/></svg>Umbrella</span>
      <span class="service"><svg><use href="#tick-box"/></svg>Renters</span>
    </li>
    <li class="service-row">
      <span class="service"><svg><use href="#tick-box"/></svg>Commercial</span>
      <span class="service"><svg><use href="#tick-box"/></svg>RV</span>
      <span class="service"><svg><use href="#tick-box"/></svg>Mobile Homes</span>
    </li>
  </ul>

  <p class="call-line">CALL NOW : <span class="phone">555-014-2290</span></p>

  <div class="contact-row">
    <span class="contact-item">
      <svg viewBox="0 0 16 16"><rect width="16" height="16" rx="3" fill="#00AB8E"/><rect x="3" y="4.5" width="10" height="7" fill="none" stroke="#fff" stroke-width="1"/><path d="M3 4.5 L8 9 L13 4.5" fill="none" stroke="#fff" stroke-width="1"/></svg>
      hello@harborshield.example
    </span>
    <span class="contact-item">
      <svg viewBox="0 0 16 16"><rect width="16" height="16" rx="3" fill="#00AB8E"/><path d="M8 13.5 C5 10 4.5 8.5 4.5 7 A3.5 3.5 0 0 1 11.5 7 C11.5 8.5 11 10 8 13.5 Z" fill="#fff"/><circle cx="8" cy="7" r="1.4" fill="#00AB8E"/></svg>
      123 Street&nbsp; Lorem Ipsum 100e
    </span>
  </div>
</main>
</body>
</html>
```